Organic skincare label - minimalist, earthy, luxe design needed!

I need a label design for a luxury natural skin care line called "Velka Botanix". Velka means 'earth' in Swahili. I would like the design to embody an earthy feel but be minimalistic and give a luxe vibe. My first product will be a Tumeric and Neem Scrub.

The size of the jar is 8oz, label dimensions should be (1.625" Tall x 8.5" Wide)
I will be making other products too such as; oils + toners so I feel free to do labels for glass bottles and/or spray bottles as well.

Forest green, light pinks/nudes/beige, grey, white, gold, are colors that can be used (not all have to be used).

I have included pictures of some things I've worked on myself as well as my original logo design but I need to simplify the logo, no circle around it.
Feel free to get creative.

Thank you! :)
Updates

Target Market(s)

Socially Conscious, Beauty Enthusiast, Minimalist

Industry/Entity Type

Skin Care

Font styles to use
Sans Serif
Other font styles liked:
• "Wonderlove doodle" is the font used for "Velka" in the logo. Feel free to use that or change it as you see fit.

Requirements
Must have
• Simplistic design
would like to stick to a font close to the ones in the logo. Either the one used for the name "Velka" OR the one that the slogan "Terra Tonics" uses.

I have also included some pictures to capture the aesthetic of my social media and website.

Gender neutral

```html
<!DOCTYPE html>
<html lang="en">
<head>
<meta charset="utf-8">
<title>Velka Botanix – Terra Tonics Label</title>
<link rel="stylesheet" href="https://fonts.googleapis.com/css2?family=Didact+Gothic&family=Pacifico&display=swap">
<style>
  :root {
    --backdrop: #3c3c3e;
    --blush: #dfc3c4;
    --paper: #ffffff;
    --band-grey: #a8a8a8;
    --sand: #cdbf9f;
    --clay: #c69c88;
    --mauve: #a8898c;
    --leaf-deep: #3e6b3a;
    --leaf-light: #8fb07f;
    --ink-soft: #5e5254;
    --ink-light: #ffffff;
    --ink-dark: #1c1c1c;
    --script: "Pacifico", cursive;
    --sans: "Didact Gothic", sans-serif;
  }
  * { box-sizing: border-box; margin: 0; padding: 0; }
  html, body {
    width: 1200px; height: 415px; overflow: hidden;
    background: var(--backdrop);
  }
  .label {
    position: absolute; left: 68px; top: 106px;
    width: 1064px; height: 204px;
    display: flex;
    font-family: var(--sans);
  }
  .panel { position: relative; width: 354.6px; height: 100%; overflow: hidden; }
  .panel--side { background: var(--blush); }
  .panel--front { background: var(--paper); }

  .copy {
    position: absolute; font-size: 9.6px; line-height: 12.4px;
    letter-spacing: 0.15px; white-space: nowrap;
  }
  .copy--muted { color: var(--ink-soft); }
  .copy--light { color: var(--ink-light); }

  .flower { position: absolute; border-radius: 46% 54% 40% 60% / 55% 45% 55% 45%; }
  .flower--left {
    left: -6px; top: 54px; width: 126px; height: 150px;
    background: radial-gradient(circle at 50% 45%, var(--clay) 0%, rgba(198,156,136,0.55) 60%, rgba(198,156,136,0) 75%);
  }
  .flower--right {
    left: 222px; top: 0; width: 134px; height: 162px;
    background: radial-gradient(circle at 50% 45%, var(--mauve) 0%, rgba(168,137,140,0.6) 60%, rgba(168,137,140,0) 75%);
  }

  .band { position: absolute; left: 0; top: 30px; width: 100%; height: 50px; background: var(--band-grey); }
  .leaf-photo {
    position: absolute; left: 4px; top: 46px; width: 340px; height: 152px;
    background: radial-gradient(ellipse at 55% 45%, var(--leaf-light) 0%, var(--leaf-deep) 45%, rgba(62,107,58,0.35) 68%, rgba(255,255,255,0) 80%);
  }
  .seal {
    position: absolute; left: 10px; top: 20px; width: 92px; height: 92px;
    border-radius: 50%; background: var(--sand);
    display: flex; align-items: center; justify-content: center;
  }
  .seal__name { font-family: var(--sans); font-size: 15px; color: var(--ink-soft); }
  .brand {
    position: absolute; left: 124px; top: 40px;
    font-family: var(--script); font-weight: 400; font-size: 26px; line-height: 40px;
    color: var(--ink-light); white-space: nowrap;
  }
  .product { position: absolute; right: 21px; top: 160px; text-align: right; color: var(--ink-dark); white-space: nowrap; }
  .product__name { font-size: 18px; line-height: 22px; }
  .product__size { font-size: 9px; line-height: 12px; }
</style>
</head>
<body>
  <div class="label">
    <section class="panel panel--side">
      <div class="flower flower--left" role="img" aria-label="Hibiscus flower illustration in warm clay tones"></div>
      <p class="copy copy--muted" style="left:26px; top:14px;">Lorem ipsum dolor sit amet, consectetuer adipiscing elit, sed<br>diam nonummy nibh euismod tincidunt ut laoreet dolore magna.<br>Lorem ipsum dolor sit amet, consectetuer adipiscing elit.</p>
      <p class="copy copy--light" style="left:130px; top:84px;">Lorem ipsum dolor sit amet, consectetuer<br>adipiscing elit, sed diam nonummy nibh<br>euismod tincidunt ut laoreet dolore magna<br>aliquam erat volutpat. Ut wisi enim ad<br>minim veniam, quis nostrud exerci tation<br>ullamcorper suscipit lobortis nisl ut aliquip<br>ex ea commodo consequat.</p>
    </section>

    <section class="panel panel--front">
      <div class="band"></div>
      <div class="leaf-photo" role="img" aria-label="Photograph of green ginkgo leaves holding water drops"></div>
      <div class="seal"><span class="seal__name">Velka</span></div>
      <h1 class="brand">Velka Botanix</h1>
      <div class="product">
        <p class="product__name">Terra Tonics</p>
        <p class="product__size">1 fl oz / 59mL</p>
      </div>
    </section>

    <section class="panel panel--side">
      <div class="flower flower--right" role="img" aria-label="Hibiscus flower illustration in muted mauve"></div>
      <p class="copy copy--muted" style="left:20px; top:14px;">Lorem ipsum dolor sit amet, consectetuer<br>adipiscing elit, sed diam nonummy nibh euismod<br>tincidunt ut laoreet dolore magna. Lorem ipsum<br>dolor sit amet, consectetuer adipiscing elit.</p>
      <p class="copy copy--light" style="left:31px; top:104px;">Ingredients: Organic Rosehip<br>Seed Oil, Organic Camellia Seed<br>Oil, Organic Pomegranate<br>Oil, VitaminE Non-GMO</p>
      <p class="copy copy--light" style="left:31px; top:170px;">MADE IN MARFA, TX</p>
    </section>
  </div>
</body>
</html>
```